Informational Trifold Flyer to Highlight Our After-School Program Curriculum

We need a trifold to hand out to families at our open house events that highlights our programs and curriculum. We provide quality, nationally recognized, award winning child development programs and after school care affordable to every family at any income level. Our programs include curriculum in Education & Career Development, STEM, the Arts, Academic Support, Character & Leadership, Health & Life Skills, Sports & Recreation.

Our curriculum is designed to be fun AND purposeful.

Our target market is parents of children ages 4-13 years old of every socioeconomic background. The brochure needs to be inclusive, eye-catching, family friendly, professional and informative.

I'm uploading our current curriculum guide for a sense of the flyer's CONTENT ONLY. Please DO NOT copy the design in the Curriculum Guide upload - we plan to redesign it soon. Please DO USE the Success Statistics in the Curriculum Guide.

I'm also uploading some of our recent flyer designs for a sense of the look and feel that we like. Also uploading our logo, some other branded assets, and a branding guideline that can be referred to for colors, fonts and logo spacing. The logo is the only required asset. The colors listed in the guideline are not required. The brand fonts are not required either but using them is a good idea, unless they just don't work with your creative vision.

I can provide logo files and other assets as psd files for final flyer.

We have around 10 flyers we need designed each year so this project can lead to regular, ongoing work.

Target Market(s)

Parents of children ages 4-13

Industry/Entity Type

Non-profit child care and child development

Font styles to use
Serif
Sans Serif
Other font styles liked:
• Franklin Gothic Book URW - Book, Franklin Gothic URW - Demi, Museo Slab - 1000, Helvetica - Regular, Arial Regular

Requirements
Must have
• Logo. Inclusive, family friendly. Ability to edit brochure based on location. Success Statistics Highlighted (see curriculum guide for content). Room for list of core programs. Quotes from parents. Register online: URL (will vary by location).
Nice to have
• It would be nice to be able to feature a few different aspects of program in detail, or show a curriculum project. Can provide content for such.
Should not have
• Anything that is not inclusive or family friendly.

```html
<!DOCTYPE html>
<html lang="en">
<head>
<meta charset="utf-8">
<title>Bright Path Academy – After School Curriculum Guide</title>
<link rel="stylesheet" href="https://fonts.googleapis.com/css2?family=Rokkitt:wght@400;600&family=Libre+Franklin:wght@400;600;700&display=swap">
<style>
:root{
  --blue:#1f8fd1;
  --blue-dark:#1672ab;
  --yellow:#f7c21b;
  --yellow-deep:#eeb00e;
  --green:#8cc63f;
  --orange:#f39a1e;
  --purple:#a56dbd;
  --teal:#3db7c8;
  --ink:#4a4a4a;
  --paper:#ffffff;
  --stage:#e4e4e4;
  --head:"Rokkitt", Georgia, serif;
  --body:"Libre Franklin", Arial, sans-serif;
}
*{box-sizing:border-box;margin:0;padding:0}
html,body{width:1200px;height:2400px;overflow:hidden}
body{background:var(--stage);font-family:var(--body);color:var(--ink);position:relative}
.spread{position:absolute;left:60px;width:1080px;height:1000px;display:flex;box-shadow:0 8px 30px rgba(0,0,0,.18)}
.spread--outside{top:150px}
.spread--inside{top:1250px}
.panel{position:relative;width:360px;height:1000px;overflow:hidden;background:var(--paper)}
.photo{position:absolute;left:0;right:0}
.wave{position:absolute;left:0;width:100%}
.head{font-family:var(--head);font-weight:600;text-transform:uppercase;letter-spacing:.5px}
p{font-size:12.5px;line-height:1.5}

/* stats panel */
.stats .photo{top:0;height:300px;background:linear-gradient(160deg,#8a6a55,#4c5f7d 55%,#a9b4c2)}
.badge{position:absolute;top:200px;right:24px;width:120px;height:120px;border-radius:50%;background:var(--yellow);border:4px solid #fff;color:#fff;text-align:center;padding-top:22px}
.badge strong{display:block;font-family:var(--head);font-size:34px;line-height:1}
.badge span{display:block;font-size:10px;line-height:1.3;padding:4px 14px 0}
.stats .content{position:absolute;top:340px;left:30px;right:30px}
.stats .head{color:var(--blue);font-size:24px;margin-bottom:8px}
.stats .intro{margin-bottom:12px}
.check-list{list-style:none}
.check-list li{display:flex;gap:10px;margin-bottom:10px;font-size:12.5px;line-height:1.45}
.check-list svg{flex:0 0 18px;margin-top:2px}
.outcomes{list-style:none;margin-top:6px}
.outcomes li{display:flex;gap:10px;margin-bottom:10px;font-size:12.5px;line-height:1.45}
.num{flex:0 0 20px;height:20px;border-radius:50%;background:var(--yellow);color:#fff;font-size:11px;font-weight:700;display:flex;align-items:center;justify-content:center;margin-top:1px}
.outcomes b{color:var(--blue-dark)}

/* mission panel */
.mission{background:var(--blue);color:#fff}
.mission .round-photo{position:absolute;top:60px;left:100px;width:160px;height:160px;border-radius:50%;border:6px solid #fff;background:linear-gradient(135deg,#c9d4e0,#5a6f8a)}
.mission .head{position:absolute;top:250px;width:100%;text-align:center;color:var(--yellow);font-size:32px}
.mission .statement{position:absolute;top:300px;left:36px;right:36px;text-align:center;font-size:13px}
.quote{position:absolute;top:420px;left:30px;right:30px;background:var(--yellow);border-radius:14px;padding:22px 22px 22px 70px;color:#fff}
.quote .mark{position:absolute;left:18px;top:6px;font-family:var(--head);font-size:70px;line-height:1}
.quote p{font-size:14px;font-style:italic}
.quote cite{display:block;margin-top:6px;font-size:12px;font-style:normal;font-weight:700}
.register{position:absolute;top:600px;left:0;right:20px;background:var(--green);border-radius:0 30px 30px 0;padding:10px 0 10px 60px;text-align:center}
.register span{display:block;font-size:11px;font-weight:700;letter-spacing:1px}
.register strong{display:block;font-size:16px}
.contact{position:absolute;top:690px;left:40px;right:30px;list-style:none}
.contact li{display:flex;align-items:center;gap:12px;font-size:15px;margin-bottom:14px}
.contact .ico{width:30px;height:30px;border-radius:50%;background:#fff;display:flex;align-items:center;justify-content:center}

/* cover panel */
.cover{background:var(--yellow)}
.cover .photo{top:0;height:470px;background:linear-gradient(150deg,#f08a3c,#5b7ca8 50%,#c4cbd6)}
.cover .title{position:absolute;top:540px;left:0;right:0;text-align:center;color:#fff;font-size:46px;line-height:1.05;font-weight:400}
.cover .base{position:absolute;bottom:0;left:0;right:0;height:240px;background:var(--blue)}
.brand{position:absolute;bottom:100px;left:0;right:0;display:flex;align-items:center;justify-content:center;gap:10px;color:#fff;font-family:var(--body);font-weight:700;font-size:26px;letter-spacing:.5px}
.brand i{width:18px;height:18px;border-radius:50%;background:#fff;display:block}
.url-bar{position:absolute;bottom:36px;left:30px;right:0;background:var(--green);color:#fff;font-weight:700;font-size:15px;padding:9px 20px;border-radius:20px 0 0 20px;text-align:center}

/* programs panel */
.programs{background:var(--blue);color:#fff}
.programs .content{position:absolute;top:50px;left:30px;right:30px}
.programs .head{color:var(--yellow);font-size:36px;margin-bottom:10px}
.programs p{margin-bottom:12px}
.programs .lead{font-size:16px;margin:6px 0 12px}
.program-list{list-style:none}
.program-list li{display:flex;gap:10px;align-items:center;margin-bottom:9px;font-size:14px}
.program-list .num{background:var(--green)}
.programs .photo{bottom:0;height:300px;background:linear-gradient(160deg,#e7c9a6,#b48c6a 50%,#7c8fa8)}

/* detail panels */
.detail .photo{top:0;height:330px}
.detail--a .photo{background:linear-gradient(150deg,#7a5a48,#c8a98e 55%,#8793a6)}
.detail--b .photo{background:linear-gradient(150deg,#d0563f,#6a88b4 55%,#d9b48f)}
.detail .content{position:absolute;top:370px;left:28px;right:28px}
.detail .tagline{font-size:34px;color:var(--yellow-deep);line-height:1;margin-bottom:16px}
.tag{display:block;color:#fff;font-size:11px;font-weight:700;letter-spacing:1px;padding:6px 12px;border-radius:0 14px 14px 0;margin:0 0 7px -28px;padding-left:28px;width:calc(100% + 28px)}
.tag--blue{background:var(--blue)}
.tag--orange{background:var(--orange)}
.tag--green{background:var(--green)}
.tag--teal{background:var(--teal)}
.tag--purple{background:var(--purple)}
.detail p{margin-bottom:14px;font-size:12px}
.circle-photo{position:absolute;border-radius:50%;border:5px solid var(--green)}
.detail--b .base{position:absolute;bottom:0;left:0;right:0;height:70px;background:var(--blue)}
</style>
</head>
<body>

<section class="spread spread--outside">
  <article class="panel stats">
    <div class="photo" role="img" aria-label="Photo of children walking down school stairs"></div>
    <svg class="wave" style="top:270px" viewBox="0 0 360 50" height="50" preserveAspectRatio="none" aria-hidden="true">
      <path d="M0 30 Q180 0 360 20 L360 50 L0 50Z" fill="#fff"/>
      <path d="M0 30 Q180 0 360 20" stroke="#8cc63f" stroke-width="4" fill="none"/>
    </svg>
    <div class="badge"><strong>87%</strong><span>of members plan to graduate and attend college</span></div>
    <div class="content">
      <h2 class="head">Success Statistics</h2>
      <p class="intro">Our members set and reach goals each year. Here is how our young people are growing.</p>
      <ul class="check-list">
        <li><svg width="18" height="18" viewBox="0 0 18 18"><circle cx="9" cy="9" r="9" fill="#8cc63f"/><path d="M5 9.5l3 3 5-6" stroke="#fff" stroke-width="2" fill="none"/></svg>87% of members say they plan to finish high school and go on to college.</li>
        <li><svg width="18" height="18" viewBox="0 0 18 18"><circle cx="9" cy="9" r="9" fill="#8cc63f"/><path d="M5 9.5l3 3 5-6" stroke="#fff" stroke-width="2" fill="none"/></svg>92% of members report that staff help them do better in school every day.</li>
        <li><svg width="18" height="18" viewBox="0 0 18 18"><circle cx="9" cy="9" r="9" fill="#8cc63f"/><path d="M5 9.5l3 3 5-6" stroke="#fff" stroke-width="2" fill="none"/></svg>78% of teen members volunteer in their community at least once a month.</li>
        <li><svg width="18" height="18" viewBox="0 0 18 18"><circle cx="9" cy="9" r="9" fill="#8cc63f"/><path d="M5 9.5l3 3 5-6" stroke="#fff" stroke-width="2" fill="none"/></svg>Members who attend often earn higher grades in reading and math than peers.</li>
      </ul>
      <h2 class="head" style="margin-top:14px">5 Priority Outcomes</h2>
      <ul class="outcomes">
        <li><span class="num">1</span><span><b>Academic Success:</b> members graduate on time, ready for college and work.</span></li>
        <li><span class="num">2</span><span><b>Good Character and Citizenship:</b> members give back and lead others.</span></li>
        <li><span class="num">3</span><span><b>Healthy Lifestyles:</b> members adopt habits that keep them well.</span></li>
      </ul>
    </div>
  </article>

  <article class="panel mission">
    <div class="round-photo" role="img" aria-label="Photo of a mentor working with students"></div>
    <h2 class="head">Our Mission</h2>
    <p class="statement">Our mission is to inspire and enable all young people, especially those who need us most, to reach their full potential as productive, caring, responsible citizens.</p>
    <blockquote class="quote">
      <span class="mark">“</span>
      <p>My child loves coming here after school, and her grades have never been better!</p>
      <cite>– Parent</cite>
    </blockquote>
    <div class="register"><span>REGISTER ONLINE:</span><strong>www.brightpathacademy.org</strong></div>
    <ul class="contact">
      <li><span class="ico"><svg width="16" height="16" viewBox="0 0 16 16"><path d="M3 1h3l1 4-2 1a8 8 0 0 0 5 5l1-2 4 1v3a2 2 0 0 1-2 2A13 13 0 0 1 1 3a2 2 0 0 1 2-2z" fill="#1f8fd1"/></svg></span>555.014.2290</li>
      <li><span class="ico"><svg width="16" height="16" viewBox="0 0 16 16"><rect x="1" y="3" width="14" height="10" rx="1" fill="#1f8fd1"/><path d="M1 4l7 5 7-5" stroke="#fff" stroke-width="1.5" fill="none"/></svg></span>info@brightpathacademy.org</li>
      <li><span class="ico"><svg width="16" height="16" viewBox="0 0 16 16"><circle cx="8" cy="8" r="6.5" stroke="#1f8fd1" stroke-width="1.5" fill="none"/><path d="M1.5 8h13M8 1.5c3 3 3 10 0 13M8 1.5c-3 3-3 10 0 13" stroke="#1f8fd1" stroke-width="1.2" fill="none"/></svg></span>www.brightpathacademy.org</li>
    </ul>
  </article>

  <article class="panel cover">
    <div class="photo" role="img" aria-label="Photo of two children playing basketball"></div>
    <svg class="wave" style="top:420px" viewBox="0 0 360 80" height="80" preserveAspectRatio="none" aria-hidden="true">
      <path d="M0 60 Q200 -10 360 20 L360 80 L0 80Z" fill="#f7c21b"/>
      <path d="M0 60 Q200 -10 360 20" stroke="#8cc63f" stroke-width="6" fill="none"/>
    </svg>
    <h1 class="head title">After School<br>Curriculum<br>Guide</h1>
    <svg class="wave" style="bottom:230px" viewBox="0 0 360 60" height="60" preserveAspectRatio="none" aria-hidden="true">
      <path d="M0 60 L0 30 Q180 -10 360 40 L360 60Z" fill="#1f8fd1"/>
      <path d="M0 30 Q180 -10 360 40" stroke="#fff" stroke-width="4" fill="none"/>
    </svg>
    <div class="base"></div>
    <div class="brand"><i></i>BRIGHT PATH ACADEMY</div>
    <div class="url-bar">www.brightpathacademy.org</div>
  </article>
</section>

<section class="spread spread--inside">
  <article class="panel programs">
    <div class="content">
      <h2 class="head">Programs</h2>
      <p>Bright Path Academy is the after school program of Westfield Youth Clubs. We offer a safe, fun place where young people learn, grow and build skills for life.</p>
      <p>We offer programs with a purpose in an affordable, safe, fun environment.</p>
      <p class="lead">Our program revolves around five core areas of focus:</p>
      <ol class="program-list">
        <li><span class="num">1</span>Education &amp; Career Development</li>
        <li><span class="num">2</span>STEM</li>
        <li><span class="num">3</span>The Arts</li>
        <li><span class="num">4</span>Academic Support</li>
        <li><span class="num">5</span>Character &amp; Leadership</li>
        <li><span class="num">6</span>Health &amp; Life Skills</li>
        <li><span class="num">7</span>Sports &amp; Recreation</li>
      </ol>
    </div>
    <div class="photo" role="img" aria-label="Photo of children painting at an easel"></div>
  </article>

  <article class="panel detail detail--a">
    <div class="photo" role="img" aria-label="Photo of students and a mentor working together"></div>
    <svg class="wave" style="top:290px" viewBox="0 0 360 50" height="50" preserveAspectRatio="none" aria-hidden="true">
      <path d="M0 50 L0 20 Q180 -5 360 30 L360 50Z" fill="#fff"/>
      <path d="M0 20 Q180 -5 360 30" stroke="#8cc63f" stroke-width="4" fill="none"/>
    </svg>
    <div class="content">
      <h2 class="head tagline">When School Out<br>We're In</h2>
      <span class="tag tag--blue">BE INSPIRED · BE CURIOUS · BE SMART</span>
      <p>Programs in Education &amp; Career Development and STEM help members explore careers, build study habits and gain skills for the future.</p>
      <span class="tag tag--orange">BE INSPIRED · BE TALENTED · BE CREATIVE</span>
      <p>Programs in the Arts let young people discover new talents in music, dance, drama and visual art while building confidence.</p>
      <span class="tag tag--teal">BE A LEADER · BE KIND · BE A FRIEND</span>
      <p>Our Character &amp; Leadership programs help members make good choices, serve their community and lead with respect.</p>
    </div>
  </article>

  <article class="panel detail detail--b">
    <div class="photo" role="img" aria-label="Photo collage of smiling club members"></div>
    <div class="circle-photo" style="top:200px;left:20px;width:110px;height:110px;background:linear-gradient(135deg,#9ab0c8,#4d617d)" role="img" aria-label="Photo of members at a table"></div>
    <div class="circle-photo" style="top:80px;right:20px;width:120px;height:120px;background:linear-gradient(135deg,#a8d0e8,#3d7fb0)" role="img" aria-label="Photo of members outdoors"></div>
    <svg class="wave" style="top:290px" viewBox="0 0 360 50" height="50" preserveAspectRatio="none" aria-hidden="true">
      <path d="M0 50 L0 30 Q180 -5 360 20 L360 50Z" fill="#fff"/>
      <path d="M0 30 Q180 -5 360 20" stroke="#1f8fd1" stroke-width="4" fill="none"/>
    </svg>
    <div class="content" style="top:360px">
      <span class="tag tag--blue">BELIEVE YOU CAN ACHIEVE</span>
      <p>Daily Academic Support gives every member help with homework, reading and math from caring staff and trained volunteers.</p>
      <span class="tag tag--purple">BE HEALTHY · BE ACTIVE · BE STRONG</span>
      <p>Programs in Health &amp; Life Skills teach members to eat well, stay active and build healthy relationships for life.</p>
      <span class="tag tag--green">BE A TEAM · BE FIT · BE A CHAMPION</span>
      <p>Sports &amp; Recreation programs build teamwork, fitness and sportsmanship through games, leagues and fun outdoor play.</p>
    </div>
    <div class="base"></div>
  </article>
</section>

</body>
</html>
```